依頼概要
〇依頼の目的/概要
電子書籍(lumora)の表紙デザインをおねがいします。

〇画像サイズ
表紙サイズの理想的な寸法は2560×1600ピクセルです。
注:画像の寸法は1000×625ピクセル以上であることが必要です。
画像の最大の寸法は10000×10000ピクセルです。

〇タイトル
夜更けの庭で青い灯をさがす旅の物語です!

〇帯キャッチ

・眠ることも許されない
死にたくなるようなかゆみと痛みから
柔らかい潤いのある肌になった

・人生の波と家族とのご縁をひもといて
薬を使わずに治す

・「絶対に治る、治ったら
同じように苦しんでいる人の為に役立つ本を書こう」
・・・と決めていました。

デザイナーさんの判断で、
どれかを使ってもらっても、
または全部を使ってもらってもOKです。

〇著者 ぽんたるべカフェ 占導師 千景(柴崎奈緒)

文字の大きさと配置と色のインパクトがあって一目惚れしました。
修正依頼にも迅速な対応もありがたかったです。

初めての電子書籍の執筆と初めてのワークベリーへの仕事依頼で、
ドキドキで、いろいろ小さなわからないところだらけでした。
たくさんの提案、どれも素敵なものばかりですべての提案者の方々に
感謝の氣持ちでいっぱいです。ありがとうございました。
これからもアトピー性皮膚炎を克服するための電子書籍を執筆していく予定なので
また、協力していただけたら嬉しいです。

```html
<!DOCTYPE html>
<html lang="ja">
<head>
<meta charset="utf-8">
<title>夜更けの庭で青い灯をさがす旅の物語です!</title>
<link rel="stylesheet" href="https://fonts.googleapis.com/css2?family=Noto+Sans+JP:wght@500;700;900&display=swap">
<style>
  :root {
    --bg-light: #ecccc1;
    --bg-mid: #c99a8e;
    --bg-dark: #9c6d63;
    --title-red: #c8102e;
    --title-edge: #ffffff;
    --ink: #1a1a1a;
    --sub-ink: #3a3030;
    --band-yellow: #fde85a;
    --band-yellow-deep: #f9d93a;
    --accent-red: #d4141c;
    --art-pink: #e98a9c;
    --art-light: #f6c6cf;
  }
  html, body {
    margin: 0;
    padding: 0;
    width: 750px;
    height: 1200px;
    overflow: hidden;
    background: #ffffff;
  }
  .cover {
    position: relative;
    width: 750px;
    height: 1200px;
    overflow: hidden;
    background:
      radial-gradient(ellipse 520px 460px at 50% 50%, var(--bg-light) 0%, var(--bg-mid) 60%, var(--bg-dark) 100%);
    font-family: "Noto Sans JP", sans-serif;
  }
  .title-heading { margin: 0; }
  .title-column {
    position: absolute;
    writing-mode: vertical-rl;
    font-weight: 900;
    color: var(--title-red);
    line-height: 1;
    text-shadow:
      0 0 3px var(--title-edge), 0 0 3px var(--title-edge),
      2px 2px 0 var(--title-edge), -2px -2px 0 var(--title-edge),
      2px -2px 0 var(--title-edge), -2px 2px 0 var(--title-edge);
  }
  .title-column--first {
    left: 608px;
    top: 10px;
    font-size: 66px;
    letter-spacing: 6px;
  }
  .title-column--second {
    left: 355px;
    top: 4px;
    font-size: 68px;
    letter-spacing: 16px;
  }
  .title-column--third {
    left: 30px;
    top: 40px;
    font-size: 100px;
    letter-spacing: 16px;
  }
  .dot-rows {
    position: absolute;
    left: 0;
    top: 0;
  }
  .heart-art {
    position: absolute;
    left: 238px;
    top: 585px;
    width: 274px;
    height: 240px;
  }
  .subtitle {
    position: absolute;
    left: 0;
    top: 805px;
    width: 750px;
    text-align: center;
    font-weight: 500;
    font-size: 27px;
    line-height: 1.35;
    color: var(--sub-ink);
    margin: 0;
  }
  .obi {
    position: absolute;
    left: 0;
    top: 925px;
    width: 750px;
    height: 275px;
    background: linear-gradient(180deg, var(--band-yellow) 0%, var(--band-yellow-deep) 100%);
    padding: 6px 0 0 18px;
    box-sizing: border-box;
    font-weight: 900;
    color: var(--ink);
  }
  .obi-line {
    margin: 0;
    line-height: 1.15;
    white-space: nowrap;
  }
  .obi-line--sleep { font-size: 44px; }
  .obi-line--pain { font-size: 41px; letter-spacing: -1px; }
  .obi-line--skin { font-size: 70px; letter-spacing: -2px; line-height: 1.05; }
  .obi-line--became { font-size: 34px; font-weight: 700; }
  .accent { color: var(--accent-red); }
  .author {
    margin: 0;
    font-size: 27px;
    font-weight: 700;
    color: var(--accent-red);
    line-height: 1.2;
    white-space: nowrap;
  }
  .author-paren { font-size: 22px; }
</style>
</head>
<body>
<main class="cover">
  <svg class="dot-rows" width="750" height="500" viewBox="0 0 750 500" aria-hidden="true">
    <g fill="#ffffff">
      <circle cx="288" cy="95" r="7"/>
      <circle cx="288" cy="140" r="7"/>
      <circle cx="288" cy="185" r="7"/>
      <circle cx="288" cy="230" r="7"/>
      <circle cx="288" cy="275" r="7"/>
      <circle cx="288" cy="320" r="7"/>
      <circle cx="525" cy="30" r="7"/>
      <circle cx="525" cy="75" r="7"/>
      <circle cx="525" cy="120" r="7"/>
      <circle cx="525" cy="165" r="7"/>
      <circle cx="525" cy="210" r="7"/>
    </g>
  </svg>

  <h1 class="title-heading">
    <span class="title-column title-column--first">夜更けの庭で青い</span>
    <span class="title-column title-column--second">灯をさがす旅の</span>
    <span class="title-column title-column--third">物語です!</span>
  </h1>

  <svg class="heart-art" viewBox="0 0 274 240" role="img" aria-label="水彩風のピンクのハートのイラストと手書きの英字メッセージ">
    <defs>
      <radialGradient id="artFill" cx="50%" cy="45%" r="55%">
        <stop offset="0%" stop-color="var(--art-light)"/>
        <stop offset="70%" stop-color="var(--art-pink)" stop-opacity="0.8"/>
        <stop offset="100%" stop-color="var(--art-pink)" stop-opacity="0"/>
      </radialGradient>
    </defs>
    <rect x="0" y="0" width="274" height="240" rx="120" fill="url(#artFill)"/>
  </svg>

  <p class="subtitle">人生の波と家族とのご縁をひもといて<br>薬を使わずに治す</p>

  <section class="obi">
    <p class="obi-line obi-line--sleep">眠ることも<span class="accent">許</span>されない</p>
    <p class="obi-line obi-line--pain">死にたくなるような<span class="accent">かゆみ</span>と<span class="accent">痛み</span>から</p>
    <p class="obi-line obi-line--skin">柔らかい潤いのある肌</p>
    <p class="obi-line obi-line--became">になった</p>
    <p class="author">【著】ぽんたるべカフェ占導師 千景<span class="author-paren">(柴崎奈緒)</span></p>
  </section>
</main>
</body>
</html>
```